Spa brochure design

I need a brochure for my day spa boutique

Here is a new and approved services I do I took it from my website....

Velvet Meadow Signature Facials are customized for all skin types, they include steam, cleanse, tone, exfoliate, extractions, massage of neck, shoulders, head, hands and arms, masque, serum, moisturizer and sun protect...your skin will be radiant, healthy and glowing.  You will instantly notice the difference in the overall tone and texture of your skin. (60 mins) add on a Micro Dermabrasion, Peel or both.  Treatments and Services we provide are:

 

Velvet Meadow Facials 

Velvet Meadow Signature Facials:

Our Signature Facial is 60 minutes of pure heaven for only $60.00  - add on a Micro Dermabrasion, a Peel or both for just $30.00 each.

Velvet Meadow Oxygen Facials:

The Oxygen Facial can give you a detoxifying facial which is excellent for clearing pollutants and toxins from the skin thus improving cell function and increasing oxygen intake it achieve complete, immediate and visible results absolutely perfect for those who have an event to go to. Deep lines and visible wrinkles fade with regular treatment. (75 min) $130.00 

Velvet Meadow Oxygen Micro Facial:

This treatment can give you a detoxifying Oxygen Facial which is excellent for clearing pollutants and toxins from the skin thus improving cell function and increasing oxygen intake. It combines the healing effects of oxygen and serum into one treatment by boosting oxygen levels, the result is a younger, fresher looking skin this plus regular stimulation and micro-circulation of needed exfoliation aids in the production of new collagen and elastinformulation and achieve complete, immediate and visible results deep lines and visible wrinkles fade with regular treatment. $175.00  

Velvet Meadow Back Facial:

A soothing and relaxing treatment for the back especially helps with breakouts and gets rid of impurities where you can't always reach includes cleanse, tone, steam, exfoliate, extractions, masque, moisturizer and sun protection. (45 min) $45.00

Facial on the Rocks:

A Velvet Meadow Signature Facial with added warm stones that makes it that much more relaxing.
(60 min)  $95.00

Teen or On the Go Facial:

Cleansing of the skin, steam, extractions, masque, moisturizer, sun protection (30 min) $45.00

 Add on to any Facial Enzyme Treatment or Specialty Masque $10.00 

Microdermabrasion & Facial Peels

Renewal Microdermabrasion Facial:

A beautiful anti aging treatment that is a exfoliating and resurfacing treatment geared towards those with hyper-pigmentation, fine lines and wrinkles includes: A customized facial for all skin types also face, neck and shoulder massage. (70 min)  $90.00

Renewal Microdermabrasion Treatment:

exfoliating treatment that is a resurfacing treatment, perfect for those with larger pores, hyper-pigmentation,fine lines, and wrinkles also helps with elasticity includes: cleansing, a masque, moisturizer, and sun protection.
(30 min) $60.00

Rejuvenate Glycolic Acid Peel Treatment:

Perfect for normal to dry skin types intensive but safe treatment designed to rapidly exfoliate skin cells, reduces appearance of fine lines, wrinkles and sun damage includes: cleansing, masque, moisturizer, and sun protection. (30 min)  $55.00

Rejuvenate Salicylic Acid Peel Treatment:

Great for oily or acne skin types. This peel exfoliates the pores to allow natural oil production and helps to get sebum production under control includes: cleansing, masque, moisturizer and sun protection. (30 min)  $55.00

Velvet Meadow Massage

Swedish Massage (60 min, 70 min and 90 min)
Aromatherapy Massage $75.00
Deep Tissue Massage $80.00
Pregnancy Massage $70.00
Massage on the Rocks $90.00

Stress Relief Treatment:

A Deep Massage of the Neck, Shoulders and Scalp (15 min) $15.00 (add on to any facial for a $1.00 a minute)

Happy Feet:

Massage and Reflexology of your tired feet (30 min) $30.00  

Waxing Services

Eye Brow Shaping and Trimming  $15.00
Eye Brow Clean-Up $10.00
Lip or Chin $10.00
Face Wax (lip/brow shaping/ chin) $30.00
Side Burns $15.00
Arm Wax:  1/2 arm $25.00 Full are $50.00
Under Arm $25.00
Bikini Wax Starting at $30.00+
Legs 1/2 $30.00+ Full legs $50+
Back Wax $50+

Nail Treatments

Manicure
Pedicure
Foot Detox
Silk Wrap
Hand and Foot Massage and Mask Treatment
Gel Nail 
Polinova Frenchie Manicure $40.00
Polinova Manicure  $35.00
Polinova Pedicure $50.00
Polinova Frenchie Pedicure $60.00
Manicure on the Rocks

Add to any Nail Service:  Polinova $10.00Frenchie $6.00, Hand polish change $8.00, Cut down $2.00, Toe polish change $12.00, One nail repair $5.00, Paraffin Hand Treatment $10.00Foot Treatment $15.00

Eye Lash Treatments

Eye Lash Tinting:

Make your own lashes stand out  "No more fake lashes and glue stuck to your eyes" (30 min) $30.00

Eye Brow Tinting:

Make your brows look Perfect 'No more penciling them in" (30 min) $20.00

For Both Eye Lash and Eye Brow Tinting:

$40.00

Here's my packages....

Velvet Meadow Signature Facials are customized for all skin types, they include steam, cleanse,tone, exfoliate, extractions, massage of neck, shoulders, head, hands and arms, masque, serum, moisturizer and sun protect...your skin will be radiant, healthy and glowing.  You'll instantly notice the difference in the overall tone and texture of you skin. (60 mins) add on a Microdermabrasion, Peel, or both.  Book in for one of beautiful Treatment Packages or Purchase a Treatment Package below as a gift, our treatments include:

Nora Whitcombe Package:

Our 75 minute Swedish Massage combined with both a hand paraffin treatment and a foot detox treatment for a revitalizing experience valued at $225.00 now only $125.00.

Lillian Garroway Package:

Enjoy a Luxury Spa Manicure then a Spa Pedicure at the same time, as a Quillora Botanic Signature Facial that will stimulate all your senses head to toe, and a Stress relief Treatment our regular price is valued at $220.00 now only $170.00.

Rosalind Tepper Package:

Our ultimate Relaxing Pearl Drift Package is our  favorite treatment combined together into one Package includes an Oxygen Facial,  Spa Manicure, Pedicure, and a 60 minute Swedish Massage is valued at $300.00 now only $210.00.

Industry/Entity Type

Boutique

Font styles to use
Serif
Decorative
Script

Requirements
Must have
• My spa and boutiques service,prices, products we use and retail, logo,and have purple and white for colors on brochure.

```html
<!DOCTYPE html>
<html lang="en">
<head>
<meta charset="utf-8">
<title>Velvet Meadow Boutique &amp; Spa – Brochure</title>
<link rel="stylesheet" href="https://fonts.googleapis.com/css2?family=Arimo:ital,wght@0,400;0,700;1,700&display=swap">
<style>
  :root {
    --purple: #8a62a8;
    --purple-deep: #6f4a92;
    --purple-soft: #c9b3dc;
    --ink: #3a3a3a;
    --white: #ffffff;
    --stage: #e4e4e4;
    --skin: #e6c2ac;
    --stone: #8d8a84;
  }
  * { margin: 0; padding: 0; box-sizing: border-box; }
  html, body { width: 1200px; height: 900px; overflow: hidden; }
  body {
    background: var(--stage);
    font-family: "Arimo", Arial, sans-serif;
    color: var(--ink);
    position: relative;
  }
  .brochure {
    position: absolute; left: 177px; top: 152px;
    width: 842px; height: 596px;
    background: var(--white);
    box-shadow: 0 2px 8px rgba(0,0,0,.15);
  }
  .brochure-art { position: absolute; inset: 0; }
  .panel { position: absolute; top: 0; height: 596px; }
  .panel-services { left: 0; width: 281px; }
  .panel-about { left: 281px; width: 280px; }
  .panel-cover { left: 561px; width: 281px; }

  .section-title {
    position: absolute; left: 18px;
    font-size: 9.5px; font-weight: 700; color: var(--purple);
  }
  .price-list {
    position: absolute; left: 18px; width: 190px;
    list-style: none; font-size: 6.4px; font-weight: 700; line-height: 8.4px;
  }
  .price { color: var(--purple); }
  .addons {
    position: absolute; left: 18px; width: 186px;
    font-size: 5.6px; font-weight: 700; line-height: 7.3px;
  }
  .treatment-title {
    position: absolute; left: 18px;
    font-size: 7.6px; font-weight: 700; color: var(--purple);
  }
  .treatment-text {
    position: absolute; left: 18px; width: 236px;
    font-size: 6.6px; font-weight: 700; line-height: 8.6px;
  }

  .owner-name {
    position: absolute; left: 160px; top: 52px;
    font-size: 9.5px; font-weight: 700; color: var(--purple);
  }
  .mission {
    position: absolute; left: 38px; top: 97px; width: 200px;
    font-size: 7.2px; font-weight: 700; line-height: 9.6px; text-align: justify;
  }
  .hours-title {
    position: absolute; left: 38px; top: 161px;
    font-size: 9.5px; font-weight: 700; color: var(--purple);
  }
  .hours {
    position: absolute; left: 38px; top: 176px; list-style: none;
    font-size: 8.6px; font-weight: 700; line-height: 11.8px; color: #111;
  }
  .hours .time { color: var(--purple); }
  .hours-note {
    position: absolute; left: 38px; top: 226px;
    font-size: 6.2px; font-weight: 700; color: #111;
  }
  .cancel-note {
    position: absolute; left: 38px; top: 243px; width: 200px;
    font-size: 6px; font-weight: 700; line-height: 7.8px; color: var(--purple);
  }
  .welcome {
    position: absolute; left: 0; top: 292px; width: 280px; text-align: center;
    font-size: 8.6px; font-weight: 700; font-style: italic; line-height: 14px; color: var(--purple);
  }
  .products {
    position: absolute; left: 31px; top: 389px; width: 222px;
    color: var(--white); font-size: 7px; font-weight: 700; line-height: 12px;
  }
  .products h2 { font-size: 8.8px; margin-bottom: 6px; }
  .products p { margin-bottom: 12px; }
  .products .facials { text-align: justify; line-height: 12.2px; }

  .brand {
    position: absolute; left: 0; top: 397px; width: 281px; text-align: center;
    font-size: 26px; font-weight: 400; color: var(--purple-deep);
  }
  .brand-mark {
    display: inline-block; width: 14px; height: 14px; border-radius: 50%;
    background: var(--purple); margin-right: 8px; vertical-align: 2px;
  }
  .contact-box {
    position: absolute; left: 53px; top: 473px; width: 179px; height: 39px;
    border: 1.5px solid var(--purple); border-radius: 20px;
    text-align: center; font-size: 8.4px; font-weight: 700; line-height: 12px;
    color: var(--purple); padding-top: 6px;
  }
  .website {
    position: absolute; left: 0; top: 536px; width: 281px; text-align: center;
    font-size: 7.4px; font-weight: 700; color: var(--purple);
  }
</style>
</head>
<body>
<main class="brochure">
  <svg class="brochure-art" width="842" height="596" viewBox="0 0 842 596" aria-hidden="false">
    <defs>
      <linearGradient id="footFade" x1="0" y1="0" x2="0" y2="1">
        <stop offset="0" stop-color="#ffffff"/>
        <stop offset="1" stop-color="#8a62a8"/>
      </linearGradient>
      <linearGradient id="skinTone" x1="0" y1="0" x2="1" y2="1">
        <stop offset="0" stop-color="#f3dccd"/>
        <stop offset="1" stop-color="#d9ab8f"/>
      </linearGradient>
      <linearGradient id="stoneTone" x1="0" y1="0" x2="1" y2="0">
        <stop offset="0" stop-color="#e9e6ea"/>
        <stop offset="0.5" stop-color="#8d8a84"/>
        <stop offset="1" stop-color="#f2f0f4"/>
      </linearGradient>
    </defs>

    <!-- services panel -->
    <path role="img" aria-label="Photo of hands applying lotion to a bare shoulder" fill="url(#skinTone)"
          d="M0 0 H281 V175 C200 155 80 150 0 150 Z"/>
    <path d="M0 150 C80 150 200 155 281 176" fill="none" stroke="#8a62a8" stroke-width="4"/>
    <line x1="18" y1="286" x2="198" y2="286" stroke="#8a62a8" stroke-width="2"/>
    <line x1="18" y1="441" x2="198" y2="441" stroke="#8a62a8" stroke-width="2"/>
    <circle role="img" aria-label="Photo of a manicure in progress" cx="228" cy="286" r="31" fill="#ecd4c6" stroke="#8a62a8" stroke-width="2.5"/>
    <circle role="img" aria-label="Photo of hands with a flower" cx="228" cy="365" r="31" fill="#e3bfa4" stroke="#8a62a8" stroke-width="2.5"/>
    <circle role="img" aria-label="Photo of eyelash tinting" cx="228" cy="441" r="31" fill="#d8c5bb" stroke="#8a62a8" stroke-width="2.5"/>
    <rect x="0" y="553" width="281" height="43" fill="url(#footFade)"/>

    <!-- about panel -->
    <rect x="281" y="0" width="280" height="596" fill="#8a62a8"/>
    <path d="M281 0 H561 V228 A140 140 0 0 1 281 228 Z" fill="#ffffff"/>
    <circle role="img" aria-label="Portrait photo of the spa owner" cx="380" cy="58" r="27" fill="#c8b1a6" stroke="#ddd" stroke-width="1.5"/>

    <!-- cover panel -->
    <rect role="img" aria-label="Photo of a relaxed woman resting with eyes closed" x="561" y="0" width="281" height="250" fill="url(#skinTone)"/>
    <path role="img" aria-label="Photo of spa stones, rolled towels and purple flowers"
          d="M575 250 C640 190 740 160 842 155 V325 C760 335 660 310 590 260 Z" fill="url(#stoneTone)"/>
    <path d="M575 250 C640 190 740 160 842 155" fill="none" stroke="#8a62a8" stroke-width="4"/>
    <path d="M590 260 C660 310 760 335 842 325" fill="none" stroke="#8a62a8" stroke-width="4"/>
    <rect x="561" y="553" width="281" height="43" fill="url(#footFade)"/>
  </svg>

  <section class="panel panel-services">
    <h2 class="section-title" style="top:183px">Waxing Services</h2>
    <ul class="price-list" style="top:196px">
      <li>Eye Brow Shaping and Trimming <span class="price">$15.00</span></li>
      <li>Eye Brow Clean-Up <span class="price">$10.00</span></li>
      <li>Lip or Chin <span class="price">$10.00</span></li>
      <li>Face Wax (lip/brow shaping/ chin) <span class="price">$30.00</span></li>
      <li>Side Burns <span class="price">$15.00</span></li>
      <li>Arm Wax: 1/2 arm $25.00 Full are <span class="price">$50.00</span></li>
      <li>Under Arm <span class="price">$25.00</span></li>
      <li>Bikini Wax Starting at <span class="price">$30.00+</span></li>
      <li>Legs 1/2 <span class="price">$30.00+</span> Full legs <span class="price">$50+</span></li>
      <li>Back Wax <span class="price">$50+</span></li>
    </ul>

    <h2 class="section-title" style="top:293px">Nail Treatments</h2>
    <ul class="price-list" style="top:306px">
      <li>Manicure</li>
      <li>Pedicure</li>
      <li>Foot Detox</li>
      <li>Silk Wrap</li>
      <li>Hand and Foot Massage and Mask Treatment</li>
      <li>Gel Nail</li>
      <li>Polinova Frenchie Manicure <span class="price">$40.00</span></li>
      <li>Polinova Manicure <span class="price">$35.00</span></li>
      <li>Polinova Pedicure <span class="price">$50.00</span></li>
      <li>Polinova Frenchie Pedicure <span class="price">$60.00</span></li>
      <li>Manicure on the Rocks</li>
    </ul>
    <p class="addons" style="top:402px">Add to any Nail Service: Polinova $10.00, Frenchie $6.00 Hand polish change $8.00, Cut down $2.00, Toe polish change $12.00, One nail repair $5.00, Paraffin Hand Treatment $10.00 Foot Treatment $15.00</p>

    <h2 class="section-title" style="top:451px">Eye Lash Treatments</h2>
    <h3 class="treatment-title" style="top:470px">Eye Lash Tinting:</h3>
    <p class="treatment-text" style="top:482px">Make your own lashes stand out "No more fake lashes and glue stuck to your eyes" (30 min) <span class="price">$30.00</span></p>
    <h3 class="treatment-title" style="top:506px">Eye Brow Tinting:</h3>
    <p class="treatment-text" style="top:518px">Make your brows look Perfect 'No more penciling them in" (30 min) <span class="price">$20.00</span></p>
    <h3 class="treatment-title" style="top:542px">For Both Eye Lash and Eye Brow Tinting - <span style="color:var(--ink)">$40.00</span></h3>
  </section>

  <section class="panel panel-about">
    <p class="owner-name">Dana Korvel</p>
    <p class="mission">Our mission at Velvet Meadow is to inspire you to look and feel better about yourself, while having the relaxing experience a big spa can offer in a small spa setting. You will get the one one attention you deserve with the experience and know how to get your desired results.</p>
    <h2 class="hours-title">My Hours:</h2>
    <ul class="hours">
      <li>Sunday - <span class="time">Closed</span></li>
      <li>Monday - Tuesday - Thursday - <span class="time">10-8</span></li>
      <li>Wednesday - Friday - <span class="time">10-5</span></li>
      <li>Saturday - <span class="time">9-5</span></li>
    </ul>
    <p class="hours-note">Earlier and later appointments available on request</p>
    <p class="cancel-note">24 hour cancellation notice if you don't show up / no call it's half the price of your service you booked for the first time after that it is full price of your service booked.</p>
    <p class="welcome">Come In and Visit our Spa Boutique<br>Walk-Ins Welcome !</p>
    <div class="products">
      <h2>PRODUCTS</h2>
      <p>Skin Care lines we carry are:</p>
      <p>QUILLORA BOTANIC skincare and Solenne Skin skincare<br>Make-up line is MAREVIA<br>Nail line is LUMARA and Corabelle Polinova</p>
      <p class="facials">Velvet Meadow Signature Facials are customized for all skin types, they include steam, cleanse, tone, exfoliate, extractions, massage of neck, shoulders, head, hands, and arms, masque, serum, moisturizer, and sun protect your skin will be radiant, healthy and glowing. You'll instantly notice the difference in the overall tone and texture of you skin. (60 min) add on a Microdermabrasion, Peel, or both.</p>
    </div>
  </section>

  <section class="panel panel-cover">
    <h1 class="brand"><span class="brand-mark"></span>Velvet Meadow</h1>
    <p class="contact-box">your address - your phone number<br>your email</p>
    <p class="website">www.velvetmeadowspa.com</p>
  </section>
</main>
</body>
</html>
```